Corvella Project

Project Description
This presentation is to Corvella (www.corvella-example.com)
We are a physician’s group practice that is trying to convince Corvella that we have the systems in place to service their clients in Assisted Living Facilities. (ALF’s)
We have to convince them in this presentation, that we have controls in place to curtail over utilization of services in general and more specifically averting clients from using the Emergency room as their primary care provider. I've included the content that needs to be included in the slides. We need to document and graphically display the message that we can effectively manage their patients in this unique environment of Assisted Living Facilities.
We also have a unique opportunity to bring some new business on board if we get this contract. We may be able to bring several thousand patients unto Corvella who previously weren’t enrolled with the carrier. We’d like to highlight that opportunity using some type of graphic art.

My presentation is due Friday, August 21, 2012.

Target Market(s)

Medical Directors (Physicians) and Health Care Attorneys

Industry/Entity Type

Environment

Requirements
Must have
• Graphics that mirror the message
Should not have
• Corvella Logo.

```html
<!DOCTYPE html>
<html lang="en">
<head>
<meta charset="utf-8">
<title>Corvella – Hospital Diversion Slides</title>
<link rel="stylesheet" href="https://fonts.googleapis.com/css2?family=Open+Sans:wght@400;600&family=Source+Sans+3:wght@400;600&display=swap">
<style>
:root{
  --page:#ffffff;
  --purple:#6b3f9c;
  --purple-soft:#9b7fc8;
  --orange:#f29b2a;
  --orange-light:#f7b85a;
  --blue:#1c5aa8;
  --navy:#123f86;
  --teal:#1fa9a4;
  --teal-light:#4cc7bf;
  --ink:#1d1d1d;
  --photo-a:#d9c7b4;
  --photo-b:#b79b86;
}
*{box-sizing:border-box;margin:0;padding:0}
html,body{width:1200px;height:675px;overflow:hidden;background:var(--page)}
body{position:relative;font-family:"Source Sans 3","Open Sans",sans-serif}
.slide{position:absolute;width:330px;height:251px;background:#fff;box-shadow:0 1px 4px rgba(0,0,0,.35);overflow:hidden}
.slide--purple{--bar:var(--purple);--accent:var(--orange);--accent-light:var(--orange-light);--lead:var(--purple-soft);--foot:var(--orange)}
.slide--blue{--bar:var(--blue);--accent:var(--teal);--accent-light:var(--teal-light);--lead:var(--navy);--foot:var(--teal)}
.s1{left:33px;top:45px}.s2{left:432px;top:45px}.s3{left:828px;top:45px}.s4{left:33px;top:338px}
.header{position:absolute;left:0;top:0;width:330px;height:42px;background:var(--bar)}
.header__photo{position:absolute;left:0;top:0;width:62px;height:42px;background:linear-gradient(135deg,var(--photo-a),var(--photo-b));border-right:2px solid #fff}
.header__title{position:absolute;right:8px;top:12px;color:#fff;font:400 15px "Open Sans",sans-serif}
.header__rule{position:absolute;left:0;top:42px;width:330px;height:4px;background:var(--accent)}
.footer{position:absolute;left:0;bottom:0;width:330px;height:6px;background:var(--foot);color:#fff;font-size:3.6px;text-align:center;line-height:6px}
.brand{position:absolute;right:6px;bottom:10px;display:flex;flex-direction:column;align-items:center;gap:2px}
.brand__mark{width:8px;height:8px;background:var(--bar)}
.brand__name{font:600 6px "Source Sans 3",sans-serif;color:var(--bar);letter-spacing:.3px}
.chart{position:absolute;left:0;top:0;width:330px;height:251px}
.node{position:absolute;background:linear-gradient(var(--accent-light),var(--accent));color:#fff;font-size:4.3px;line-height:5.4px;padding:1px 3px;border:.5px solid #fff}
.node--lead{background:var(--lead);text-align:center;font-size:5px;line-height:10px;padding:0}
.node--center{text-align:center}
.goals{position:absolute;left:8px;top:54px;width:300px;color:var(--ink);font-size:8.3px;line-height:9.6px}
.goals h3{font-weight:400;color:var(--accent);font-size:8.6px;margin:0 0 1px;display:flex;align-items:center;gap:4px}
.goals h3::before{content:"";width:5px;height:5px;background:var(--bar)}
.goals ol{list-style:none;counter-reset:g;margin-bottom:7px}
.goals li{counter-increment:g;position:relative;padding-left:15px}
.goals li::before{content:counter(g)".";position:absolute;left:0;color:var(--accent)}
</style>
</head>
<body>

<!-- Slide 1: flow, purple -->
<section class="slide slide--purple s1">
  <div class="header"><div class="header__photo" role="img" aria-label="Photo of a caregiver with a young patient"></div><h2 class="header__title">Hospital Diversion</h2></div>
  <div class="header__rule"></div>
  <div class="chart">
    <svg width="330" height="251" style="position:absolute;left:0;top:0" aria-hidden="true">
      <g stroke="var(--accent)" stroke-width="1" fill="none">
        <path d="M165 63V78H100M165 78H195"/>
        <path d="M140 92V102M235 92V96"/>
        <path d="M140 124V138M250 118V126M250 162V167"/>
        <path d="M140 197V206H100M140 166V172M140 182V187"/>
        <path d="M250 188V200M150 210H195M59 85V203"/>
      </g>
    </svg>
    <div class="node node--lead" style="left:120px;top:51px;width:90px;height:12px">Assisted Living Facility Staff</div>
    <div class="node" style="left:18px;top:73px;width:82px">911 Telephone Call</div>
    <div class="node" style="left:195px;top:70px;width:82px">Emergency Response Button<br>Replacing 911 / RMS Personnel</div>
    <div class="node" style="left:95px;top:102px;width:90px">PCMH – Medical Home Triage<br>RMS Triage Staff</div>
    <div class="node" style="left:210px;top:96px;width:82px">Psychiatric Rapid Response Team<br>Task Force / RMS Staff</div>
    <div class="node node--center" style="left:95px;top:138px;width:100px">LOCAL HOSPITAL EMERGENCY DEPARTMENT</div>
    <div class="node" style="left:197px;top:126px;width:93px">Rapid Intervention Protocols<br>Chemical Restraints<br>Psychiatrist On Call<br>RMS Personnel On-Site</div>
    <div class="node node--center" style="left:95px;top:156px;width:100px">EMERGENCY ROOM DOCTOR</div>
    <div class="node node--center" style="left:115px;top:172px;width:70px">HOSPITALIST</div>
    <div class="node" style="left:197px;top:167px;width:93px">Psych-Care<br>Capitated</div>
    <div class="node node--center" style="left:95px;top:187px;width:100px">SNF: Skilled Nursing Facility</div>
    <div class="node" style="left:18px;top:203px;width:82px">Home / Assisted Living Facility<br>Follow-up visit post ER Visit<br>Textline Text Msg to Owners Daily</div>
    <div class="node" style="left:195px;top:203px;width:82px">Home / Assisted Living Facility<br>Follow-up visit post ER Visit<br>Textline Text Msg to Owners Daily</div>
  </div>
  <div class="brand"><span class="brand__mark"></span><span class="brand__name">MERIDIAN</span></div>
  <div class="footer">Caring for People – Committed to Family – Connected to Community</div>
</section>

<!-- Slide 2: goals, purple -->
<section class="slide slide--purple s2">
  <div class="header"><div class="header__photo" role="img" aria-label="Photo of a caregiver with a young patient"></div></div>
  <div class="header__rule"></div>
  <div class="goals">
    <h3>Short Term Goals:</h3>
    <ol>
      <li>Demonstrating our network efficiencies while providing quality care</li>
      <li>Showcasing our creativity and innovation in curtailing overutilization</li>
      <li>Demonstrating our tracking and monitoring systems across different environments.</li>
      <li>Introduction of new business in historically fee for service environments -APD</li>
    </ol>
    <h3>Long Term Goals:</h3>
    <ol>
      <li>Demonstrating the benefits of identifying ALF clients in the same way hospitalized and Rehab clients are targeted for better clinical outcomes</li>
      <li>Determination of Assisted Living Facilities as a niche market, that is underserved.</li>
      <li>Demonstrating how better ALF management = lower SNF admissions.</li>
      <li>Becoming the provider of choice for ALF consumers</li>
    </ol>
  </div>
  <div class="brand"><span class="brand__mark"></span><span class="brand__name">MERIDIAN</span></div>
  <div class="footer">Caring for People – Committed to Family – Connected to Community</div>
</section>

<!-- Slide 3: flow, blue -->
<section class="slide slide--blue s3">
  <div class="header"><div class="header__photo" role="img" aria-label="Photo of a caregiver with a young patient"></div><h2 class="header__title">Hospital Diversion</h2></div>
  <div class="header__rule"></div>
  <div class="chart">
    <svg width="330" height="251" style="position:absolute;left:0;top:0" aria-hidden="true">
      <g stroke="var(--accent)" stroke-width="1" fill="none">
        <path d="M165 63V78H100M165 78H195"/>
        <path d="M140 92V102M235 92V96"/>
        <path d="M140 124V138M250 118V126M250 162V167"/>
        <path d="M140 197V206H100M140 166V172M140 182V187"/>
        <path d="M250 188V200M150 210H195M59 85V203"/>
      </g>
    </svg>
    <div class="node node--lead" style="left:120px;top:51px;width:90px;height:12px">Assisted Living Facility Staff</div>
    <div class="node" style="left:18px;top:73px;width:82px">911 Telephone Call</div>
    <div class="node" style="left:195px;top:70px;width:82px">Emergency Response Button<br>Replacing 911 / RMS Personnel</div>
    <div class="node" style="left:95px;top:102px;width:90px">PCMH – Medical Home Triage<br>RMS Triage Staff</div>
    <div class="node" style="left:210px;top:96px;width:82px">Psychiatric Rapid Response Team<br>Task Force / RMS Staff</div>
    <div class="node node--center" style="left:95px;top:138px;width:100px">LOCAL HOSPITAL EMERGENCY DEPARTMENT</div>
    <div class="node" style="left:197px;top:126px;width:93px">Rapid Intervention Protocols<br>Chemical Restraints<br>Psychiatrist On Call<br>RMS Personnel On-Site</div>
    <div class="node node--center" style="left:95px;top:156px;width:100px">EMERGENCY ROOM DOCTOR</div>
    <div class="node node--center" style="left:115px;top:172px;width:70px">HOSPITALIST</div>
    <div class="node" style="left:197px;top:167px;width:93px">Psych-Care<br>Capitated</div>
    <div class="node node--center" style="left:95px;top:187px;width:100px">SNF: Skilled Nursing Facility</div>
    <div class="node" style="left:18px;top:203px;width:82px">Home / Assisted Living Facility<br>Follow-up visit post ER Visit<br>Textline Text Msg to Owners Daily</div>
    <div class="node" style="left:195px;top:203px;width:82px">Home / Assisted Living Facility<br>Follow-up visit post ER Visit<br>Textline Text Msg to Owners Daily</div>
  </div>
  <div class="brand"><span class="brand__mark"></span><span class="brand__name">MERIDIAN</span></div>
  <div class="footer"></div>
</section>

<!-- Slide 4: goals, blue -->
<section class="slide slide--blue s4">
  <div class="header"><div class="header__photo" role="img" aria-label="Photo of a caregiver with a young patient"></div></div>
  <div class="header__rule"></div>
  <div class="goals">
    <h3>Short Term Goals:</h3>
    <ol>
      <li>Demonstrating our network efficiencies while providing quality care</li>
      <li>Showcasing our creativity and innovation in curtailing overutilization</li>
      <li>Demonstrating our tracking and monitoring systems across different environments.</li>
      <li>Introduction of new business in historically fee for service environments -APD</li>
    </ol>
    <h3>Long Term Goals:</h3>
    <ol>
      <li>Demonstrating the benefits of identifying ALF clients in the same way hospitalized and Rehab clients are targeted for better clinical outcomes</li>
      <li>Determination of Assisted Living Facilities as a niche market, that is underserved.</li>
      <li>Demonstrating how better ALF management = lower SNF admissions.</li>
      <li>Becoming the provider of choice for ALF consumers</li>
    </ol>
  </div>
  <div class="brand"><span class="brand__mark"></span><span class="brand__name">MERIDIAN</span></div>
  <div class="footer"></div>
</section>

</body>
</html>
```